Logo + Business Card Design Project

We are looking at changing our logo and reprinting business cards.

Attached is a design concept for the logo (we have no hi res files for this).

The logo needs to be able to work standalone without the tagline.

We are happy for you to use this concept or design a new one. The existing concept is quite well liked.

We would also consider not having Systems in the logo and just have KRW Systems Pty Ltd in the body text of the card.

We have a Tag Line that needs to go on all documentation / websites etc wherever the logo appears.

Tagline: Lifting tech higher

Our message to clients is that we have solutions that:

KRW Systems:
Lifting tech higher

Turning up Revenue
Turning up Profit
Turning up Confidence

We would require the files in a High Res format for print and a scalable transparent format for web.
(We also need greyscale and monochrome files)
All source files need to be delivered with existing layers etc

A corporate guide with the logo usage and colours should be specified.

Suggestions:
The new logo has to have CMYK colours of 100 90 0 0

CMYK 100 90 0 0
RGB #21409A
Websafe #224499
Greyscale #414141

We would also need a business card layout designed.
Could be one sided or 2 sided. Will probably print matt cello 2 sides on 350gsm gloss
Updates

Industry/Entity Type

Business

Requirements
Should not have
• Lower case n in KRW.

```html
<!DOCTYPE html>
<html lang="en">
<head>
<meta charset="utf-8">
<title>KRW Systems – Logo and Business Card</title>
<link rel="stylesheet" href="https://fonts.googleapis.com/css2?family=Open+Sans:wght@400;600;700;800&display=swap">
<style>
  :root {
    --brand-blue: #21409a;
    --ink: #231f20;
    --paper: #ffffff;
    --faint: #e4e4e4;
    --backdrop: #262626;
  }
  * { box-sizing: border-box; margin: 0; padding: 0; }
  html, body { width: 849px; height: 1200px; overflow: hidden; }
  body {
    position: relative;
    background: var(--backdrop);
    font-family: "Open Sans", Arial, sans-serif;
    color: var(--ink);
  }

  /* ---------- Card front ---------- */
  .card-front {
    position: absolute; left: 100px; top: 165px;
    width: 380px; height: 230px;
    background: var(--paper); overflow: hidden;
  }
  .card-front .swoosh { position: absolute; inset: 0; }
  .card-front .wordmark {
    position: absolute; left: 28px; top: 36px;
    color: var(--brand-blue); font-weight: 800; line-height: 1;
  }
  .wordmark .mark-name { display: block; font-size: 72px; letter-spacing: -2px; }
  .wordmark .mark-sub  { display: block; font-size: 18px; letter-spacing: 6px; margin-top: 4px; }
  .card-front .tagline {
    position: absolute; left: 30px; top: 170px;
    font-size: 15px; font-weight: 600; color: var(--ink);
  }
  .card-front .holder {
    position: absolute; right: 20px; top: 158px; text-align: right; color: var(--paper);
  }
  .holder .holder-name  { font-size: 13px; font-weight: 700; }
  .holder .holder-title { font-size: 11px; }

  /* ---------- Card back ---------- */
  .card-back {
    position: absolute; left: 296px; top: 390px;
    width: 356px; height: 216px;
    background: var(--paper); overflow: hidden;
  }
  .card-back .faint-name {
    position: absolute; left: 14px; top: 4px;
    color: var(--faint); font-weight: 800; line-height: 1;
  }
  .faint-name .mark-name { display: block; font-size: 64px; letter-spacing: -2px; }
  .faint-name .mark-sub  { display: block; font-size: 17px; letter-spacing: 6px; margin-top: 2px; }
  .contact {
    position: absolute; top: 106px;
    display: grid; grid-template-columns: 44px auto; column-gap: 4px;
    font-size: 8px; line-height: 12px;
  }
  .contact-left  { left: 31px; }
  .contact-right { left: 162px; padding-left: 12px; border-left: 1px solid var(--ink); height: 54px; }
  .contact dt, .contact dd { height: 12px; white-space: nowrap; }
  .card-back .band {
    position: absolute; left: 0; bottom: 0; width: 100%; height: 55px;
    background: var(--brand-blue); color: var(--paper); text-align: center;
  }
  .band .messages { font-size: 10px; margin-top: 4px; }
  .band .tagline  { font-size: 12px; font-weight: 600; margin-top: 8px; }

  /* ---------- Logo panel ---------- */
  .logo-panel { position: absolute; left: 0; top: 0; }
  .logo-lockup {
    position: absolute; left: 426px; top: 850px;
    color: var(--brand-blue); font-weight: 800; line-height: 1;
  }
  .logo-lockup .mark-name { display: block; font-size: 82px; letter-spacing: -2px; }
  .logo-lockup .mark-sub  { display: block; font-size: 22px; letter-spacing: 9px; margin-top: 8px; }
  .logo-tagline {
    position: absolute; left: 428px; top: 982px;
    font-size: 20px; font-weight: 600; color: var(--ink); line-height: 1.2;
  }
</style>
</head>
<body>

  <section class="card-front" aria-label="Business card front">
    <svg class="swoosh" width="380" height="230" viewBox="0 0 380 230" aria-hidden="true">
      <path d="M112 230 C 180 160, 270 140, 380 118 L 380 230 Z" fill="var(--brand-blue)"/>
    </svg>
    <div class="wordmark">
      <span class="mark-name">KRW</span>
      <span class="mark-sub">SYSTEMS</span>
    </div>
    <p class="tagline">Lifting tech higher</p>
    <div class="holder">
      <p class="holder-name">Daniel Whitcombe</p>
      <p class="holder-title">Project Director</p>
    </div>
  </section>

  <section class="card-back" aria-label="Business card back">
    <div class="faint-name" aria-hidden="true">
      <span class="mark-name">KRW</span>
      <span class="mark-sub">SYSTEMS</span>
    </div>
    <dl class="contact contact-left">
      <dt>Phone</dt><dd>+61 2 5550-4100</dd>
      <dt>Support</dt><dd>+61 2 5550-4133</dd>
      <dt>Fax</dt><dd>+61 2 5550-4101</dd>
      <dt>Mobile</dt><dd>0400 555 218</dd>
    </dl>
    <dl class="contact contact-right">
      <dt>Email</dt><dd>daniel.whitcombe@krw.com.au</dd>
      <dt>Web</dt><dd>www.krw.com.au</dd>
      <dt>Address</dt><dd>12/40 Harlow Street</dd>
      <dt>&nbsp;</dt><dd>Northbridge NSW 2063</dd>
    </dl>
    <div class="band">
      <p class="messages">Better Revenue&nbsp; - &nbsp;Better Margins&nbsp; - &nbsp;Better Certainty</p>
      <p class="tagline">Lifting tech higher</p>
    </div>
  </section>

  <svg class="logo-panel" width="849" height="1200" viewBox="0 0 849 1200" aria-hidden="true">
    <polygon points="372,818 849,738 849,1092 305,1055" fill="var(--paper)"/>
  </svg>
  <div class="logo-lockup">
    <span class="mark-name">KRW</span>
    <span class="mark-sub">SYSTEMS</span>
  </div>
  <p class="logo-tagline">Lifting tech higher</p>

</body>
</html>
```